LABEL for Extra Virgin Olive oil

Hi everyone!
I would please like your help with the below project.

We will start importing olive oil from Greece and I would like to create the label for the bottle.
Our goal is to create a label that will really promote the raw quality of the natural product (olive oil).
The olive oil we will import will be very high quality, but we don't want the label to promote a luxury product but more just an exceptional quality natural product that is for the many and comes directly from the producer. Potentially the label can also include images (ex. oils, olive trees, land, sea, sun) but we can evaluate that along the way.
The approximate size of the label will be 60x110 mm
The colors should be earth colors
We can discuss any potential questions as soon as we are in contact.

Thank you all in advance for your time and consideration.

Kind regards, Tobias

```html
<!DOCTYPE html>
<html lang="en">
<head>
<meta charset="UTF-8">
<title>Extra Virgin Olive Oil Label</title>
<link rel="stylesheet" href="https://fonts.googleapis.com/css2?family=Montserrat:wght@400;500;700&family=Crimson+Text:wght@400&family=Kaushan+Script&display=swap">
<style>
  :root {
    --page-bg: #ffffff;
    --label-bg: #d9cdab;
    --ink: #2e2e2e;
    --pill-text: #f2ecdc;
    --art-tone: #b9ad8c;
    --art-tone-soft: #cfc29f;
  }
  html, body {
    margin: 0;
    padding: 0;
    width: 900px;
    height: 1200px;
    overflow: hidden;
    background: var(--page-bg);
  }
  .canvas {
    position: relative;
    width: 900px;
    height: 1200px;
  }
  .label {
    position: absolute;
    left: 155px;
    top: 59px;
    width: 590px;
    height: 1082px;
    background: var(--label-bg);
    border-radius: 18px;
    overflow: hidden;
    color: var(--ink);
    text-align: center;
  }
  .origin {
    position: absolute;
    top: 50px;
    left: 0;
    right: 0;
    font-family: "Montserrat", sans-serif;
    font-weight: 400;
    font-size: 21px;
    letter-spacing: 5px;
    margin: 0;
  }
  .tree-art {
    position: absolute;
    top: 113px;
    left: 181px;
    width: 228px;
    height: 197px;
    border-radius: 50% 50% 8px 8px;
    background: radial-gradient(ellipse at 50% 40%, var(--art-tone) 0%, var(--art-tone-soft) 70%, var(--label-bg) 100%);
  }
  .tagline {
    position: absolute;
    top: 330px;
    left: 0;
    right: 0;
    margin: 0;
    font-family: "Montserrat", sans-serif;
    font-weight: 500;
    font-size: 20px;
    line-height: 28px;
    letter-spacing: 1.5px;
  }
  .divider {
    position: absolute;
    top: 430px;
    left: 0;
    width: 590px;
    height: 26px;
  }
  .grade {
    position: absolute;
    top: 500px;
    left: 0;
    right: 0;
    margin: 0;
    font-family: "Crimson Text", serif;
    font-size: 33px;
    letter-spacing: 1.5px;
    font-weight: 400;
  }
  .product-name {
    position: absolute;
    top: 540px;
    left: 0;
    right: 0;
    margin: 0;
    font-weight: 400;
  }
  .product-name .script {
    display: block;
    font-family: "Kaushan Script", cursive;
    font-size: 128px;
    line-height: 150px;
    margin-left: -20px;
  }
  .product-name .serif {
    position: absolute;
    top: 142px;
    left: 338px;
    font-family: "Crimson Text", serif;
    font-size: 46px;
    letter-spacing: 2px;
    line-height: 50px;
  }
  .method {
    position: absolute;
    top: 840px;
    left: 184px;
    width: 222px;
    height: 34px;
    border-radius: 17px;
    background: var(--ink);
    color: var(--pill-text);
    font-family: "Montserrat", sans-serif;
    font-weight: 500;
    font-size: 19px;
    line-height: 34px;
    letter-spacing: 0.5px;
  }
  .volume {
    position: absolute;
    top: 990px;
    left: 0;
    right: 0;
    margin: 0;
    font-family: "Montserrat", sans-serif;
    font-weight: 700;
    font-size: 25px;
  }
  .branch-art {
    position: absolute;
    background: linear-gradient(160deg, var(--art-tone-soft) 0%, var(--art-tone) 60%, var(--label-bg) 100%);
    opacity: 0.7;
  }
  .branch-art.left {
    left: 0;
    top: 840px;
    width: 140px;
    height: 242px;
    border-radius: 0 70px 0 0;
  }
  .branch-art.right {
    right: 0;
    top: 855px;
    width: 178px;
    height: 227px;
    border-radius: 90px 0 0 0;
  }
</style>
</head>
<body>
<main class="canvas">
  <section class="label">
    <p class="origin">FROM GREECE</p>
    <div class="tree-art" role="img" aria-label="Line illustration of an olive tree standing on a small hill"></div>
    <p class="tagline">STRAIGHT FROM THE<br>PRODUCER</p>
    <svg class="divider" viewBox="0 0 590 26" preserveAspectRatio="none" aria-hidden="true">
      <polygon fill="var(--ink)" points="0,10 40,7 90,11 150,6 210,10 260,5 320,9 380,4 440,8 500,5 560,9 590,7 590,20 540,17 480,21 420,16 360,20 300,17 240,21 180,16 120,20 60,17 0,21"/>
    </svg>
    <p class="grade">EXTRA VIRGIN</p>
    <h1 class="product-name"><span class="script">Olive</span><span class="serif">OIL</span></h1>
    <div class="method">COLD PRESSED</div>
    <p class="volume">750ml</p>
    <div class="branch-art left" role="img" aria-label="Line illustration of an olive branch with leaves and olives"></div>
    <div class="branch-art right" role="img" aria-label="Line illustration of an olive sprig with olives"></div>
  </section>
</main>
</body>
</html>
```